Medical Marihuana Packaging Design

We seek skilled packaging designer for sales unit box for client of ours.

Unit is a metall tiin with outlay label in paper. The seeked design is: minimal, modern, coloring according to logo and ci of company (see attachment).

The product contained insales unit is medical marihuana which will be retailed to public.

Note: We dont need any marihuana leafs or signs. We need pharma related , moderm, serious, cutting edge design.

website: www.velorimpha.ch

Please check all attachments prior to posting ans questions, thx

Target Market(s)

young audience

Industry/Entity Type

Pharmaceutical

Font styles to use
Sans Serif

Colors
9bcb3c
acd037
cadf82
ffffff

Requirements
Must have
• Logo, corporate colors
Should not have
• No Marihuana Leafs or symbols

```html
<!DOCTYPE html>
<html lang="en">
<head>
<meta charset="utf-8">
<title>Velorimpha – Tin Label</title>
<link rel="stylesheet" href="https://fonts.googleapis.com/css2?family=Open+Sans:wght@300;700&display=swap">
<style>
  :root {
    --label-green: #4b6a2f;
    --label-green-deep: #3f5b26;
    --accent-lime: #9bcb3c;
    --accent-pale: #cadf82;
    --rule-dark: #2c431b;
    --silver-light: #f4f4f4;
    --silver-mid: #c9c9c9;
    --silver-dark: #a9a9a9;
    --ink-brand: #2f4a1e;
    --white: #ffffff;
  }
  html, body {
    margin: 0;
    padding: 0;
    width: 1199px;
    height: 1200px;
    overflow: hidden;
    background: var(--label-green);
  }
  .label {
    position: relative;
    width: 1199px;
    height: 1200px;
    background: linear-gradient(180deg, var(--label-green) 0%, var(--label-green-deep) 100%);
    font-family: "Open Sans", Arial, sans-serif;
  }
  .accent-line {
    position: absolute;
    left: 0; right: 0;
    top: 100px;
    height: 5px;
    background: linear-gradient(90deg, var(--accent-lime), var(--accent-pale), var(--accent-lime));
  }
  .silver {
    background: linear-gradient(90deg, var(--silver-dark) 0%, var(--silver-light) 35%, var(--silver-mid) 60%, var(--silver-light) 85%, var(--silver-dark) 100%);
  }
  .brand-band {
    position: absolute;
    left: 0; right: 0;
    top: 170px;
    height: 250px;
  }
  .rule {
    position: absolute;
    left: 0; right: 0;
    height: 5px;
    background: var(--rule-dark);
  }
  .rule--upper { top: 205px; }
  .rule--lower { top: 385px; }
  .brand-band__foot {
    position: absolute;
    left: 0; right: 0;
    top: 420px;
    height: 40px;
  }
  .brand {
    position: absolute;
    left: 0; right: 0;
    top: 210px;
    height: 175px;
    display: flex;
    align-items: center;
    justify-content: center;
    gap: 28px;
  }
  .brand__dot {
    width: 82px;
    height: 82px;
    border-radius: 50%;
    background: var(--ink-brand);
  }
  .brand__name {
    font-weight: 300;
    font-size: 96px;
    letter-spacing: 4px;
    color: var(--ink-brand);
    line-height: 1;
  }
  .product {
    position: absolute;
    left: 0; right: 0;
    top: 740px;
    display: flex;
    justify-content: center;
  }
  .product__box {
    display: flex;
    flex-direction: column;
    align-items: stretch;
    gap: 10px;
  }
  .product__rule {
    height: 4px;
    background: var(--silver-light);
  }
  .product__rule-pair {
    display: flex;
    flex-direction: column;
    gap: 8px;
  }
  .product__name {
    font-weight: 700;
    font-size: 68px;
    color: var(--white);
    line-height: 1.1;
    padding: 0 6px;
  }
  .emblem {
    position: absolute;
    left: 50%;
    bottom: 0;
    transform: translateX(-50%);
  }
</style>
</head>
<body>
  <main class="label">
    <div class="accent-line"></div>

    <div class="brand-band silver"></div>
    <div class="rule rule--upper"></div>
    <div class="rule rule--lower"></div>
    <div class="brand-band__foot silver"></div>

    <div class="brand">
      <span class="brand__dot"></span>
      <span class="brand__name">VELORIMPHA</span>
    </div>

    <section class="product">
      <div class="product__box">
        <div class="product__rule"></div>
        <div class="product__name">Marihuana</div>
        <div class="product__rule-pair">
          <div class="product__rule"></div>
          <div class="product__rule"></div>
        </div>
      </div>
    </section>

    <svg class="emblem" width="240" height="120" viewBox="0 0 240 120" role="img" aria-label="Silver triangular panel with geometric key pattern">
      <polygon points="120,0 240,120 0,120" fill="#dcdcdc"/>
    </svg>
  </main>
</body>
</html>
```